PPT template for boutique strategic planning, accounting and taxation firm

We are a boutique firm that provides strategic, accounting and tax advice to our clients. The work we are doing is increasingly strategic work and we are required to produce reports and presentations and our current templates are simply not sufficient.
As you can see from the examples attached, we have very limited skills in house re design! We have attached a PPT document and word document (that should be PPT) that we use regularly as examples of the content. Excel worksheets are regularly embedded into the presentation (in both blue and orange - see below re colours)
Not specific to one area but typically these clients are famous for their own brand and are creating value in their industry through creating their own brand and we want to produce documents of a similar standard.
A Powerpoint Document Slide Template
Cover page layout, back page, intermediate page heading, in colours and styles based on the logo, title styles, and an intermediate or chapter heading slide style. Many of our presentations contain slides with tables, diagrams, flowcharts and text, including simple lists of bullet points. As above, you will see in our style guide that we have three coloured logos – we would like one version in blue and one version in orange please. Again, the cover should be bold and draw attention but remain professional.
We are looking for something that works in both 4:3 and 16:9 (or two templates please)
We like a clear professional and simple look.
Deliverable: PowerPoint template file (.potx extension) for PowerPoint 2007 with at least a “cover” layout, a “title and content” layout, and a simplified slide layout, as well as “back cover”. Please embed any fonts used.
Target Market(s)
Many of our clients are retail clients or have strong brands of their own.
Industry/Entity Type
Accounting
Requirements
Must have
- Harrowby & Co logo on each page.
Must have a cover page (please be bold but professional)
A selection of "standard" slides - dot points, detailed written content, example diagrams, flow charts etc.
A back cover
Nice to have
- We would like to have a copy done in both the blue and orange versions attached. Happy for the winner to complete the other colour after the winner is selected.
Prefer Arial logo but open to suggestions. Must be easy to read and professional
Should not have
- Nothing cartoonish

```html
<!DOCTYPE html>
<html lang="en">
<head>
<meta charset="utf-8">
<title>Harrowby &amp; Co — Presentation Template</title>
<link rel="stylesheet" href="https://fonts.googleapis.com/css2?family=Alfa+Slab+One&family=Cinzel:wght@400;700&family=Open+Sans:wght@400;700&display=swap">
<style>
  :root{
    --canvas:#ffffff;
    --paper:#efece4;
    --paper-edge:#e4e0d6;
    --sky:#2a9fdc;
    --blue:#1f6cb5;
    --navy:#0c2a5c;
    --ink:#2b2b2b;
    --rule:#3a3a3a;
    --muted:#55524c;
  }
  *{box-sizing:border-box;margin:0;padding:0}
  html,body{width:1200px;height:900px;overflow:hidden;background:var(--canvas)}
  body{position:relative;font-family:"Open Sans",Arial,sans-serif;color:var(--ink)}

  .slide{
    position:absolute;overflow:hidden;
    background:radial-gradient(ellipse at 40% 40%,#f4f2ec 0%,var(--paper) 60%,var(--paper-edge) 100%);
    box-shadow:0 2px 5px rgba(0,0,0,.45);
  }
  .slide--big{width:437px;height:250px}
  .slide--small{width:321px;height:180px}

  /* header */
  .slide-title{position:absolute;font-family:"Alfa Slab One",Georgia,serif;color:var(--sky);letter-spacing:.3px;line-height:1;text-transform:uppercase;white-space:nowrap;transform:scaleX(.8);transform-origin:left top}
  .slide--big .slide-title{left:23px;top:15px;font-size:25px}
  .slide--small .slide-title{left:20px;top:9px;font-size:17px}
  .title-rule{position:absolute;height:2px;background:var(--rule)}
  .slide--big .title-rule{left:20px;top:44px;width:360px}
  .slide--small .title-rule{left:18px;top:28px;width:265px}
  .title-marker{position:absolute;border:1.5px solid var(--blue);border-radius:50%;background:var(--paper)}
  .title-marker::after{content:"";position:absolute;left:50%;top:50%;width:5px;height:5px;background:var(--navy);transform:translate(-50%,-50%) rotate(45deg)}
  .slide--big .title-marker{left:3px;top:38px;width:13px;height:13px}
  .slide--small .title-marker{left:3px;top:23px;width:11px;height:11px}

  .corner{position:absolute;color:#fff;font-family:"Alfa Slab One",Georgia,serif}
  .corner--top{right:0;top:0;background:var(--blue);clip-path:polygon(0 0,100% 0,100% 100%)}
  .slide--big .corner--top{width:50px;height:40px;font-size:9px;text-align:right;padding:8px 12px 0 0}
  .slide--small .corner--top{width:36px;height:28px;font-size:7px;text-align:right;padding:5px 8px 0 0}
  .corner--bottom{right:0;bottom:0;background:var(--blue);clip-path:polygon(100% 0,100% 100%,0 100%);display:flex;align-items:flex-end;justify-content:flex-end}

  .content-title{position:absolute;font-family:"Cinzel",Georgia,serif;font-size:11px;font-weight:400;color:var(--ink)}
  .slide--small .content-title{font-size:9px}

  .body-copy{position:absolute;font-family:"Cinzel",Georgia,serif;font-size:3.6px;line-height:5.2px;color:var(--muted)}
  .body-copy p{margin-bottom:3px}
  .chevron{position:absolute;width:12px;height:10px;background:var(--blue);clip-path:polygon(0 0,55% 0,100% 50%,55% 100%,0 100%,40% 50%)}

  .brand{position:absolute;display:flex;align-items:center;gap:3px;font-family:"Open Sans",Arial,sans-serif;font-weight:700;color:var(--navy);white-space:nowrap}
  .brand-dot{border-radius:50%;background:var(--navy)}
  .brand--footer{font-size:5.5px}
  .brand--footer .brand-dot{width:6px;height:6px}

  /* cover */
  .cover{left:175px;top:28px;width:437px;height:247px}
  .cover-visual{position:absolute;left:5px;top:7px;width:427px;height:130px;
    background:linear-gradient(135deg,#0a2a6e 0%,#1a6fc8 55%,#0b2f78 100%)}
  .cover-band{position:absolute;left:0;top:140px;width:100%;height:5px;background:var(--blue)}
  .cover-url{position:absolute;left:12px;bottom:6px;font-size:6px;color:var(--muted)}
  .cover .brand{right:40px;bottom:8px;font-size:10px}
  .cover .brand-dot{width:12px;height:12px}
  .cover .corner--bottom{width:38px;height:40px;font-size:13px;padding:0 6px 3px 0}

  /* two-column */
  .two-column{left:175px;top:300px}
  .col-divider{position:absolute;left:207px;top:70px;width:2px;height:155px;background:var(--blue)}

  .with-image{left:175px;top:567px}
  .image-slot{position:absolute;left:300px;top:85px;width:108px;height:111px;background:var(--blue)}
  .image-badge{position:absolute;left:528px;top:765px;width:81px;height:81px;border-radius:50%;background:#1c1c1c;color:#fff;display:flex;align-items:center;justify-content:center;font-family:"Cinzel",Georgia,serif;font-size:8.5px}

  .graphic{left:637px;top:70px}
  .text-only{left:637px;top:265px}
  .bullets{left:637px;top:462px}
  .thanks{left:637px;top:650px}

  .bullet-head{position:absolute;left:38px;top:42px;font-family:"Cinzel",Georgia,serif;font-size:10px;font-weight:400}
  .table-head{position:absolute;left:228px;top:42px;font-family:"Cinzel",Georgia,serif;font-size:10px;font-weight:400}
  .bullet-divider{position:absolute;left:162px;top:50px;width:1.5px;height:112px;background:var(--blue)}
  .bullet-main{position:absolute;left:30px;top:70px;font-family:"Alfa Slab One",Georgia,serif;font-size:6px;color:var(--blue);display:flex;align-items:center;gap:3px}
  .bullet-main::before{content:"";width:5px;height:5px;border:1.2px solid var(--blue);border-radius:50%}
  .sub-list{position:absolute;top:81px;list-style:none;font-family:"Cinzel",Georgia,serif;font-size:4px;color:var(--muted)}
  .sub-list li{display:flex;align-items:center;gap:2px;height:9.6px}
  .sub-list li::before{content:"";width:5px;height:5px;border-radius:50%;background:var(--navy)}
  .data-table{position:absolute;left:188px;top:60px;width:117px;height:110px;border:3px solid var(--blue);
    display:grid;grid-template-columns:1fr 1fr;grid-template-rows:repeat(6,1fr)}
  .data-table span{border:0.75px solid var(--blue)}

  .thanks-word{position:absolute;left:0;width:100%;text-align:center;font-family:"Alfa Slab One",Georgia,serif;font-size:27px;color:var(--sky);line-height:1;transform:scaleX(.82)}
  .thanks-word--main{top:82px}
  .thanks-word--reflection{top:110px;transform:scaleX(.82) scaleY(-1);opacity:.25;
    -webkit-mask-image:linear-gradient(to top,#000,transparent 70%);mask-image:linear-gradient(to top,#000,transparent 70%)}
  .thanks .brand{left:142px;bottom:3px}
  .thanks .corner--bottom{width:24px;height:26px;font-size:10px;padding:0 5px 2px 0}
</style>
</head>
<body>

<!-- Cover -->
<section class="slide cover">
  <div class="cover-visual" role="img" aria-label="Cover photograph: abstract blue light streaks"></div>
  <div class="cover-band"></div>
  <p class="cover-url">http://www.yoursitehere.com/</p>
  <div class="brand"><span class="brand-dot"></span>Harrowby &amp; Co</div>
  <div class="corner corner--bottom">01</div>
</section>

<!-- Two column content -->
<section class="slide slide--big two-column">
  <h2 class="slide-title">Slide Title</h2>
  <div class="title-rule"></div><div class="title-marker"></div>
  <div class="corner corner--top">04</div>
  <h3 class="content-title" style="left:15px;top:62px">Content Title</h3>
  <span class="chevron" style="left:16px;top:80px"></span>
  <div class="body-copy" style="left:32px;top:80px;width:165px">
    <p>Our team reviews each plan with care and sets clear goals for growth, cash flow, tax and long term value across every part of the business. Our team reviews each plan with care and sets clear goals for growth, cash flow, tax and long term value across every part of the business.</p>
    <p>Our team reviews each plan with care and sets clear goals for growth, cash flow, tax and long term value across every part of the business. Our team reviews each plan with care and sets clear goals for growth, cash flow, tax and long term value across every part of the business.</p>
    <p>Our team reviews each plan with care and sets clear goals for growth, cash flow, tax and long term value across every part of the business. Our team reviews each plan with care and sets clear goals for growth, cash flow, tax and long term value across every part of the business.</p>
    <p>Our team reviews each plan with care and sets clear goals for growth, cash flow, tax and long term value across every part of the business. Our team reviews each plan with care and sets clear goals for growth, cash flow, tax and long term value across every part of the business.</p>
  </div>
  <div class="col-divider"></div>
  <span class="chevron" style="left:222px;top:80px"></span>
  <div class="body-copy" style="left:240px;top:80px;width:165px">
    <p>Our team reviews each plan with care and sets clear goals for growth, cash flow, tax and long term value across every part of the business. Our team reviews each plan with care and sets clear goals for growth, cash flow, tax and long term value across every part of the business.</p>
    <p>Our team reviews each plan with care and sets clear goals for growth, cash flow, tax and long term value across every part of the business. Our team reviews each plan with care and sets clear goals for growth, cash flow, tax and long term value across every part of the business.</p>
  </div>
  <span class="chevron" style="left:222px;top:158px"></span>
  <div class="body-copy" style="left:240px;top:158px;width:165px">
    <p>Our team reviews each plan with care and sets clear goals for growth, cash flow, tax and long term value across every part of the business. Our team reviews each plan with care and sets clear goals for growth, cash flow, tax and long term value across every part of the business.</p>
    <p>Our team reviews each plan with care and sets clear goals for growth, cash flow, tax and long term value across every part of the business. Our team reviews each plan with care and sets clear goals for growth, cash flow, tax and long term value across every part of the business.</p>
  </div>
  <div class="brand brand--footer" style="left:180px;bottom:5px"><span class="brand-dot"></span>Harrowby &amp; Co</div>
</section>

<!-- Content with image -->
<section class="slide slide--big with-image">
  <h2 class="slide-title">Slide Title</h2>
  <div class="title-rule"></div><div class="title-marker"></div>
  <div class="corner corner--top">04</div>
  <h3 class="content-title" style="left:15px;top:60px">Content Title</h3>
  <span class="chevron" style="left:16px;top:80px"></span>
  <div class="body-copy" style="left:32px;top:80px;width:265px">
    <p>Our team reviews each plan with care and sets clear goals for growth, cash flow, tax and long term value across every part of the business. Our team reviews each plan with care and sets clear goals for growth, cash flow, tax and long term value across every part of the business.</p>
  </div>
  <div class="body-copy" style="left:16px;top:108px;width:260px">
    <p>Our team reviews each plan with care and sets clear goals for growth, cash flow, tax and long term value across every part of the business. Our team reviews each plan with care and sets clear goals for growth, cash flow, tax and long term value across every part of the business.</p>
    <p>Our team reviews each plan with care and sets clear goals for growth, cash flow, tax and long term value across every part of the business. Our team reviews each plan with care and sets clear goals for growth, cash flow, tax and long term value across every part of the business.</p>
    <p>Our team reviews each plan with care and sets clear goals for growth, cash flow, tax and long term value across every part of the business. Our team reviews each plan with care and sets clear goals for growth, cash flow, tax and long term value across every part of the business.</p>
    <p>Our team reviews each plan with care and sets clear goals for growth, cash flow, tax and long term value across every part of the business. Our team reviews each plan with care and sets clear goals for growth, cash flow, tax and long term value across every part of the business.</p>
  </div>
  <div class="image-slot" role="img" aria-label="Image placeholder"></div>
  <div class="brand brand--footer" style="left:180px;bottom:5px"><span class="brand-dot"></span>Harrowby &amp; Co</div>
</section>
<div class="image-badge">WITH IMAGE</div>

<!-- Graphic slide -->
<section class="slide slide--small graphic">
  <h2 class="slide-title">Graphic Slide</h2>
  <div class="title-rule"></div><div class="title-marker"></div>
  <div class="corner corner--top">04</div>
  <svg width="321" height="180" style="position:absolute;left:0;top:0" aria-label="Pyramid diagram and pie chart">
    <polygon points="86,70 66,92 106,92" fill="#8dc63f"/>
    <polygon points="62,96 110,96 126,121 46,121" fill="#1f6cb5"/>
    <polygon points="126,121 46,121 46,124 126,124" fill="#164f86"/>
    <polygon points="42,125 130,125 156,148 16,148" fill="#5a5d63"/>
    <polygon points="156,148 16,148 16,152 156,152" fill="#3b3d41"/>
    <g transform="translate(230,90)">
      <ellipse cx="0" cy="8" rx="42" ry="42" fill="#555"/>
      <path d="M0,0 L0,-42 A42,42 0 0 1 36.4,-21 Z" fill="#139a43"/>
      <path d="M0,0 L36.4,-21 A42,42 0 0 1 36.4,21 Z" fill="#2bb673"/>
      <path d="M0,0 L36.4,21 A42,42 0 0 1 0,42 Z" fill="#1f6cb5"/>
      <path d="M0,0 L0,42 A42,42 0 0 1 -36.4,21 Z" fill="#b08a63"/>
      <path d="M0,0 L-36.4,21 A42,42 0 0 1 -36.4,-21 Z" fill="#5f6369"/>
      <path d="M0,0 L-36.4,-21 A42,42 0 0 1 0,-42 Z" fill="#8dc63f"/>
      <g stroke="#fff" stroke-width="1.5"><line x1="0" y1="0" x2="0" y2="-42"/><line x1="0" y1="0" x2="36.4" y2="-21"/><line x1="0" y1="0" x2="36.4" y2="21"/><line x1="0" y1="0" x2="0" y2="42"/><line x1="0" y1="0" x2="-36.4" y2="21"/><line x1="0" y1="0" x2="-36.4" y2="-21"/></g>
    </g>
  </svg>
  <div class="brand brand--footer" style="left:142px;bottom:3px"><span class="brand-dot"></span>Harrowby &amp; Co</div>
</section>

<!-- Text slide -->
<section class="slide slide--small text-only">
  <h2 class="slide-title">Slide Title</h2>
  <div class="title-rule"></div><div class="title-marker"></div>
  <div class="corner corner--top">04</div>
  <h3 class="content-title" style="left:16px;top:43px">Content Title</h3>
  <div class="body-copy" style="left:16px;top:56px;width:285px;font-size:3.2px;line-height:4.6px">
    <p>Our team reviews each plan with care and sets clear goals for growth, cash flow, tax and long term value across every part of the business. Our team reviews each plan with care and sets clear goals for growth, cash flow, tax and long term value across every part of the business.</p>
    <p>Our team reviews each plan with care and sets clear goals for growth, cash flow, tax and long term value across every part of the business. Our team reviews each plan with care and sets clear goals for growth, cash flow, tax and long term value across every part of the business.</p>
    <p>Our team reviews each plan with care and sets clear goals for growth, cash flow, tax and long term value across every part of the business. Our team reviews each plan with care and sets clear goals for growth, cash flow, tax and long term value across every part of the business.</p>
    <p>Our team reviews each plan with care and sets clear goals for growth, cash flow, tax and long term value across every part of the business. Our team reviews each plan with care and sets clear goals for growth, cash flow, tax and long term value across every part of the business.</p>
    <p>Our team reviews each plan with care and sets clear goals for growth, cash flow, tax and long term value across every part of the business. Our team reviews each plan with care and sets clear goals for growth, cash flow, tax and long term value across every part of the business.</p>
  </div>
  <div class="brand brand--footer" style="left:142px;bottom:3px"><span class="brand-dot"></span>Harrowby &amp; Co</div>
</section>

<!-- Bullets and table -->
<section class="slide slide--small bullets">
  <h2 class="slide-title">Slide Title</h2>
  <div class="title-rule"></div><div class="title-marker"></div>
  <div class="corner corner--top">04</div>
  <h3 class="bullet-head">Bullet Form</h3>
  <h3 class="table-head">Table</h3>
  <div class="bullet-main">MAIN BULLET</div>
  <ul class="sub-list" style="left:42px"><li>Sub bullet</li><li>Sub bullet</li><li>Sub bullet</li><li>Sub bullet</li><li>Sub bullet</li><li>Sub bullet</li></ul>
  <ul class="sub-list" style="left:88px"><li>Sub bullet</li><li>Sub bullet</li><li>Sub bullet</li><li>Sub bullet</li><li>Sub bullet</li><li>Sub bullet</li></ul>
  <div class="bullet-divider"></div>
  <div class="data-table" role="table" aria-label="Empty two-column table">
    <span></span><span></span><span></span><span></span><span></span><span></span>
    <span></span><span></span><span></span><span></span><span></span><span></span>
  </div>
  <div class="brand brand--footer" style="left:142px;bottom:3px"><span class="brand-dot"></span>Harrowby &amp; Co</div>
</section>

<!-- Back cover -->
<section class="slide slide--small thanks">
  <p class="thanks-word thanks-word--main">THANK YOU</p>
  <p class="thanks-word thanks-word--reflection" aria-hidden="true">THANK YOU</p>
  <div class="brand brand--footer"><span class="brand-dot"></span>Harrowby &amp; Co</div>
  <div class="corner corner--bottom">X</div>
</section>

</body>
</html>
```